Business Card Tech Company
Veradon Corp
Project: Business Card Tech Company
Business Card Tech Company -
Creative Brief
Simple
Marcel Dufresne
CEO
2745 Rue Belcourt, Québec, QC G2K 3P7, Canada
mdufresne@veradoncorp-example.com
www.veradoncorp-example.com
You can add Twitter @veradoncorp We are very open to different designs, We will provide fast feedback, You can try many styles and many fonts, Right now, our slogan is: the world made yours. You can put it on some designs if it fits well, consider we might want to change it.
We would like a back mostly visual, without much info.

```html
<!DOCTYPE html>
<html lang="en">
<head>
<meta charset="utf-8">
<title>Veradon Corp – Business Card</title>
<link rel="stylesheet" href="https://fonts.googleapis.com/css2?family=Open+Sans:wght@400;600;700&display=swap">
<style>
  :root {
    --page: #e9ebee;
    --card: #ffffff;
    --blue: #1f7cc4;
    --blue-dark: #0f5a99;
    --grey: #8a8f96;
    --grey-light: #c9cdd2;
    --ink: #3b4148;
    --faint: #e6eef6;
  }
  * { margin: 0; padding: 0; box-sizing: border-box; }
  html, body { width: 1200px; height: 646px; overflow: hidden; }
  body {
    background: var(--page);
    font-family: "Open Sans", Arial, sans-serif;
    position: relative;
  }
  .card {
    position: absolute;
    top: 172px;
    width: 520px;
    height: 300px;
    background: var(--card);
    box-shadow: 0 6px 18px rgba(0,0,0,.12);
    overflow: hidden;
  }
  .card-back { left: 50px; }
  .card-front { left: 630px; }

  /* back */
  .back-mark {
    position: absolute;
    left: -70px; top: 20px;
    width: 260px; height: 260px;
    border-radius: 50%;
    background: var(--faint);
  }
  .back-name {
    position: absolute;
    left: 175px; top: 100px;
    font-weight: 700;
    font-size: 64px;
    color: var(--blue);
    letter-spacing: -1px;
    line-height: 1;
  }
  .back-web {
    position: absolute;
    left: 180px; top: 176px;
    font-size: 13px;
    letter-spacing: 2px;
    color: var(--grey);
  }

  /* front */
  .brand {
    position: absolute;
    left: 30px; top: 112px;
    display: flex; align-items: center; gap: 10px;
  }
  .brand-dot {
    width: 40px; height: 40px; border-radius: 50%;
    background: var(--blue);
  }
  .brand-name {
    font-weight: 700; font-size: 36px; color: var(--blue); line-height: 1;
    letter-spacing: -0.5px;
  }
  .person {
    position: absolute; right: 28px; top: 22px; text-align: right;
  }
  .person-name { font-weight: 700; font-size: 17px; color: var(--blue-dark); }
  .person-title { font-size: 11px; color: var(--grey); letter-spacing: 1px; }
  .waves { position: absolute; left: 0; top: 0; width: 520px; height: 300px; }
  .contact {
    position: absolute; right: 28px; top: 76px;
    list-style: none; text-align: right;
    font-size: 10.5px; line-height: 17px; color: var(--ink);
  }
  .contact li { display: flex; justify-content: flex-end; align-items: center; gap: 6px; }
  .contact svg { width: 11px; height: 11px; flex: none; }
  .contact .gap { margin-top: 5px; }
</style>
</head>
<body>

<section class="card card-back" aria-label="Card back">
  <div class="back-mark"></div>
  <div class="back-name">Veradon</div>
  <div class="back-web">www.veradoncorp-example.com</div>
</section>

<section class="card card-front" aria-label="Card front">
  <svg class="waves" viewBox="0 0 520 300" aria-hidden="true">
    <path d="M0 246 C120 272 220 258 330 232 C420 212 480 206 520 206 L520 300 L0 300 Z" fill="var(--grey-light)"/>
    <path d="M0 260 C130 286 240 270 340 244 C430 222 485 218 520 218 L520 300 L0 300 Z" fill="var(--blue)"/>
    <path d="M0 280 C140 300 260 284 360 262 C440 246 490 242 520 242 L520 300 L0 300 Z" fill="var(--blue-dark)"/>
    <path d="M0 266 C130 292 240 276 340 250 C430 228 485 224 520 224" fill="none" stroke="#ffffff" stroke-width="3"/>
  </svg>

  <div class="brand">
    <span class="brand-dot"></span>
    <span class="brand-name">Veradon</span>
  </div>

  <div class="person">
    <div class="person-name">Marcel Dufresne</div>
    <div class="person-title">CEO</div>
  </div>

  <ul class="contact">
    <li>2745 Rue Belcourt,</li>
    <li>Québec, QC G2K 3P7, Canada</li>
    <li class="gap">418 555 0142
      <svg viewBox="0 0 12 12"><path d="M3 1 L5 3.5 L4 5 C5 7 6 8 7 8.5 L8.5 7.5 L11 9.5 L10 11 C5 11 1 7 1 2 Z" fill="var(--blue)"/></svg>
    </li>
    <li>mdufresne@veradoncorp-example.com
      <svg viewBox="0 0 12 12"><rect x="1" y="2.5" width="10" height="7" fill="none" stroke="var(--blue)" stroke-width="1.3"/><path d="M1 3 L6 7 L11 3" fill="none" stroke="var(--blue)" stroke-width="1.3"/></svg>
    </li>
    <li>www.veradoncorp-example.com
      <svg viewBox="0 0 12 12"><circle cx="6" cy="6" r="4.8" fill="none" stroke="var(--blue)" stroke-width="1.3"/><path d="M1.2 6 H10.8 M6 1.2 C3.5 4 3.5 8 6 10.8 M6 1.2 C8.5 4 8.5 8 6 10.8" fill="none" stroke="var(--blue)" stroke-width="1"/></svg>
    </li>
    <li>@veradoncorp
      <svg viewBox="0 0 12 12"><rect x="1" y="1" width="10" height="10" fill="var(--blue)"/></svg>
    </li>
  </ul>
</section>

</body>
</html>
```